Brightwell Mechanical - Business Card Design

We would like a dark (likely black) themed business card to be able to hand out to potential clients. We may list our services on the card or keep it clean. Unsure. Logo attached

```html
<!DOCTYPE html>
<html lang="en">
<head>
<meta charset="UTF-8">
<title>Brightwell Mechanical – Business Card</title>
<link href="https://fonts.googleapis.com/css2?family=Oswald:wght@500&family=Work+Sans:wght@400;700&display=swap" rel="stylesheet">
<style>
  :root {
    --backdrop: #1b1b1b;
    --card: #242424;
    --card-edge: #2b2b2b;
    --blue: #2b7bd3;
    --orange: #ef6a2c;
    --white: #f2f2f2;
  }
  * { box-sizing: border-box; margin: 0; padding: 0; }
  html, body {
    width: 1200px; height: 900px; overflow: hidden;
    background: var(--backdrop);
    font-family: "Work Sans", sans-serif;
    color: var(--white);
  }
  .card {
    position: absolute; left: 250px;
    width: 700px; height: 400px;
    background: linear-gradient(135deg, var(--card) 0%, var(--card-edge) 100%);
    border-bottom: 7px solid var(--blue);
  }
  .card--front { top: 30px; }
  .card--back { top: 470px; }

  .brand {
    position: absolute; left: 60px; right: 60px; top: 165px;
    display: flex; align-items: center; justify-content: center; gap: 14px;
  }
  .brand__dot {
    width: 26px; height: 26px; border-radius: 50%;
    background: var(--orange); flex: none;
  }
  .brand__name {
    font-family: "Work Sans", sans-serif; font-weight: 700;
    font-size: 30px; letter-spacing: 1px; text-transform: uppercase;
    color: var(--blue); white-space: nowrap;
  }

  .person {
    position: absolute; left: 30px; top: 112px; width: 300px; text-align: right;
  }
  .person__name {
    font-family: "Oswald", sans-serif; font-weight: 500;
    font-size: 44px; line-height: 1; color: var(--blue);
    text-transform: uppercase; letter-spacing: 0.5px; white-space: nowrap;
  }
  .person__role { font-size: 20px; margin-top: 6px; letter-spacing: 0.5px; }
  .divider {
    position: absolute; left: 352px; top: 118px;
    width: 2px; height: 78px; background: var(--blue);
  }
  .contacts {
    position: absolute; left: 376px; top: 118px;
    list-style: none; font-size: 18px; letter-spacing: 0.8px;
  }
  .contacts li { display: flex; align-items: center; gap: 10px; height: 27px; white-space: nowrap; }
  .contacts svg { width: 14px; height: 14px; flex: none; }
  .address {
    position: absolute; left: 150px; bottom: 38px;
    font-size: 20px; letter-spacing: 1px; white-space: nowrap;
  }
</style>
</head>
<body>
  <section class="card card--front">
    <div class="brand">
      <span class="brand__dot"></span>
      <span class="brand__name">Brightwell Mechanical Inc</span>
    </div>
  </section>

  <section class="card card--back">
    <div class="person">
      <div class="person__name">Daniel Harper</div>
      <div class="person__role">Founder</div>
    </div>
    <div class="divider"></div>
    <ul class="contacts">
      <li>
        <svg viewBox="0 0 24 24" fill="var(--blue)"><path d="M6.6 10.8a15.1 15.1 0 0 0 6.6 6.6l2.2-2.2a1 1 0 0 1 1-.25 11.4 11.4 0 0 0 3.6.57 1 1 0 0 1 1 1V20a1 1 0 0 1-1 1A17 17 0 0 1 3 4a1 1 0 0 1 1-1h3.5a1 1 0 0 1 1 1c0 1.25.2 2.45.57 3.57a1 1 0 0 1-.25 1z"/></svg>
        (555) 214-7730
      </li>
      <li>
        <svg viewBox="0 0 24 24" fill="none" stroke="var(--blue)" stroke-width="2"><rect x="3" y="5" width="18" height="14" rx="1"/><path d="M3 6l9 7 9-7"/></svg>
        info@brightwellmech.com
      </li>
      <li>
        <svg viewBox="0 0 24 24" fill="none" stroke="var(--blue)" stroke-width="2"><circle cx="12" cy="12" r="9"/><path d="M3 12h18M12 3c3 3 3 15 0 18M12 3c-3 3-3 15 0 18"/></svg>
        www.brightwellmech.com
      </li>
    </ul>
    <p class="address">2418 Fenwick Lane Milwaukee, WI 53208</p>
  </section>
</body>
</html>
```